Banner ad for Gen Y demographic - Training Institute

We are a training organization that requires two (2) banner ads which we can use to promote our brand, our Diploma of Management and Diploma of Business product offerings, you may visit our website: www.pembertonlearninghub.com.au to grab some background information on us.

I have also included our logo to be used in the banner ad (white or black depending on background color). The text to be used throughout the banner ad is Times New Roman please.

We require flash banners that just have the text changing from one slide to the next. We want something clean and enticing. We also need a call to action button “Start now” or something similar.

I have included the below just as a guide but welcome any creativity that you believe would fit our market. I encourage you to be creative!

Flash panels:
1 Slide – I don’t take classes. I experience them – are you in?
2 Slide - Unlock your potential excellence today

I need two different banner ads / sizes please:

1. 600px (W) x 120px (H), max file size 150KB, gif, jpeg, swf
2. 300px(w) x 250px(h), max size 150KB, gif, jpeg, swf

Out target audience is Gen Y, they are looking for ways to improve their careers, make more money, or to get a different job at their existing employer. They’re looking for a Diploma in Management or Business that will give them the education and the piece of paper that will allow them to get that job.

I look forward to seeing what you come up with!

Industry/Entity Type

Training

```html
<!DOCTYPE html>
<html lang="en">
<head>
<meta charset="utf-8">
<title>Pemberton &amp; Associates – Banner Set</title>
<link rel="stylesheet" href="https://fonts.googleapis.com/css2?family=Tinos:ital,wght@0,400;0,700;1,400;1,700&family=Arimo:wght@400;700&display=swap">
<style>
  :root {
    --stage: #161616;
    --stage-light: #222222;
    --label: #ffffff;
    --brown-deep: #3a2207;
    --brown-mid: #6b4412;
    --gold-light: #b98a3c;
    --parchment-light: #e0a544;
    --parchment-dark: #a8691f;
    --tagline: #f2a935;
    --white: #ffffff;
    --button: #c8903c;
    --button-text: #2a1a06;
  }
  * { margin: 0; padding: 0; box-sizing: border-box; }
  html, body {
    width: 1200px;
    height: 750px;
    overflow: hidden;
  }
  body {
    position: relative;
    background: radial-gradient(ellipse at 50% 40%, var(--stage-light), var(--stage) 75%);
    font-family: "Tinos", "Times New Roman", serif;
  }
  .size-label {
    position: absolute;
    left: 0;
    width: 1200px;
    text-align: center;
    font-family: "Arimo", Arial, sans-serif;
    font-size: 18px;
    color: var(--label);
    letter-spacing: 0.5px;
  }
  .size-label--leaderboard { top: 52px; }
  .size-label--rectangle { top: 703px; }

  /* ---------- 600 x 120 banner ---------- */
  .banner-wide {
    position: absolute;
    left: 150px;
    top: 97px;
    width: 900px;
    height: 180px;
    overflow: hidden;
  }
  .banner-wide__bg { position: absolute; inset: 0; }
  .brand-mark {
    position: absolute;
    display: flex;
    flex-direction: column;
    align-items: center;
    justify-content: center;
    gap: 10px;
    color: var(--white);
    font-family: "Tinos", "Times New Roman", serif;
    font-size: 20px;
    text-align: center;
    line-height: 1.15;
  }
  .brand-mark__dot {
    width: 46px;
    height: 46px;
    border-radius: 50%;
    background: var(--white);
  }
  .banner-wide .brand-mark { left: 22px; top: 22px; width: 180px; height: 136px; }

  .headline {
    color: var(--white);
    font-family: "Tinos", "Times New Roman", serif;
    font-weight: 700;
    font-size: 42px;
    line-height: 1;
    white-space: nowrap;
  }
  .subhead {
    color: var(--white);
    font-size: 20px;
    line-height: 1;
    white-space: nowrap;
  }
  .tagline {
    color: var(--tagline);
    font-style: italic;
    font-size: 29px;
    line-height: 34px;
    white-space: nowrap;
  }
  .tagline strong { font-weight: 700; }

  .banner-wide .headline { position: absolute; right: 22px; top: 18px; }
  .banner-wide .subhead { position: absolute; left: 435px; width: 420px; text-align: center; top: 64px; }
  .banner-wide .tagline { position: absolute; left: 280px; top: 95px; }

  .cta {
    display: flex;
    align-items: center;
    justify-content: center;
    background: var(--button);
    color: var(--button-text);
    font-family: "Tinos", "Times New Roman", serif;
    font-size: 21px;
    text-decoration: none;
    letter-spacing: 0.3px;
  }
  .banner-wide .cta {
    position: absolute;
    left: 713px;
    top: 103px;
    width: 166px;
    height: 54px;
    border: 3px solid var(--white);
    border-radius: 8px;
  }

  /* ---------- 300 x 250 banner ---------- */
  .banner-box {
    position: absolute;
    left: 375px;
    top: 312px;
    width: 450px;
    height: 375px;
    overflow: hidden;
    background: radial-gradient(ellipse 75% 65% at 50% 30%, var(--gold-light), var(--brown-mid) 55%, var(--brown-deep) 100%);
    text-align: center;
  }
  .banner-box .brand-mark { left: 135px; top: 18px; width: 180px; height: 150px; }
  .banner-box .headline { position: absolute; left: 0; width: 450px; top: 170px; }
  .banner-box .subhead { position: absolute; left: 0; width: 450px; top: 211px; }
  .banner-box .tagline { position: absolute; left: 0; width: 450px; top: 238px; }
  .banner-box .cta {
    position: absolute;
    left: 141px;
    top: 324px;
    width: 167px;
    height: 48px;
    border: 3px solid var(--white);
    border-bottom: none;
    border-radius: 10px 10px 0 0;
  }
  .banner-box__baseline {
    position: absolute;
    left: 0;
    bottom: 2px;
    width: 450px;
    height: 4px;
    background: var(--white);
  }
</style>
</head>
<body>
  <p class="size-label size-label--leaderboard">600PX X 120PX</p>

  <section class="banner-wide" aria-label="600 by 120 banner">
    <svg class="banner-wide__bg" width="900" height="180" viewBox="0 0 900 180" aria-hidden="true">
      <defs>
        <linearGradient id="wide-dark" x1="0" y1="0" x2="1" y2="0.3">
          <stop offset="0" stop-color="#3a2207"/>
          <stop offset="0.6" stop-color="#4e3009"/>
          <stop offset="1" stop-color="#7a5016"/>
        </linearGradient>
        <radialGradient id="wide-parchment" cx="0.4" cy="0.45" r="0.75">
          <stop offset="0" stop-color="#e6ad4d"/>
          <stop offset="0.7" stop-color="#c9852b"/>
          <stop offset="1" stop-color="#a8691f"/>
        </radialGradient>
      </defs>
      <rect width="900" height="180" fill="url(#wide-dark)"/>
      <path d="M0 0 H270 Q196 80 172 180 H0 Z" fill="url(#wide-parchment)" role="img" aria-label="Warm parchment texture panel"/>
      <path d="M274 0 Q200 80 176 180" fill="none" stroke="#ffffff" stroke-width="7"/>
    </svg>

    <div class="brand-mark">
      <span class="brand-mark__dot"></span>
      <span>Pemberton &amp; Associates</span>
    </div>

    <h1 class="headline">Pemberton &amp; Associates</h1>
    <p class="subhead">Institute of Business and Management</p>
    <p class="tagline">I don’t take classes.<br>I experience them – <strong>are you in?</strong></p>
    <a class="cta" href="https://www.pembertonlearninghub.com.au">START NOW</a>
  </section>

  <section class="banner-box" aria-label="300 by 250 banner">
    <div class="brand-mark">
      <span class="brand-mark__dot"></span>
      <span>Pemberton &amp; Associates</span>
    </div>
    <h2 class="headline">Pemberton &amp; Associates</h2>
    <p class="subhead">Institute of Business and Management</p>
    <p class="tagline">I don’t take classes.<br>I experience them – <strong>are you in?</strong></p>
    <a class="cta" href="https://www.pembertonlearninghub.com.au">START NOW</a>
    <span class="banner-box__baseline"></span>
  </section>

  <p class="size-label size-label--rectangle">300PX X 250PX</p>
</body>
</html>
```